Velmora - New coded website

Current website is around 5 years old and corrupted in some ways...
I would like to refresh the design and to create a new coded website based on the current content .
Please refer to :
www.velmora-sample.com.au

Coded - Design and coding required

```html
<!DOCTYPE html>
<html lang="en">
<head>
<meta charset="utf-8">
<title>Velmora – Odours Controlled Naturally</title>
<link href="https://fonts.googleapis.com/css2?family=Roboto:wght@400;500;700;900&display=swap" rel="stylesheet">
<style>
:root{
  --navy:#0d1f2d;
  --btn:#0b1a33;
  --green:#7cb83a;
  --teal:#0e5a75;
  --teal-dark:#0b4a63;
  --ink:#1c2b33;
  --text:#2a2f33;
  --light:#eef0ef;
  --grey:#c5cbcc;
  --white:#ffffff;
}
*{box-sizing:border-box;margin:0;padding:0}
html,body{width:1200px;height:3046px;overflow:hidden}
body{position:relative;background:var(--white);font-family:"Roboto",sans-serif;color:var(--text)}
.abs{position:absolute}
.img-fill{position:absolute}

/* header */
.site-header{position:absolute;left:0;top:0;width:1200px;height:73px;background:var(--navy);z-index:3}
.brand{position:absolute;left:60px;top:16px;display:flex;align-items:center;gap:10px;color:var(--white);font-size:26px;font-weight:500}
.brand-dot{width:40px;height:40px;border-radius:50%;background:var(--green)}
.nav-item{position:absolute;top:24px;font-size:13px;color:var(--white);white-space:nowrap}
.nav-item.active{color:var(--green);font-weight:500}
.header-phone{position:absolute;left:1027px;top:20px;display:flex;align-items:center;gap:10px;color:var(--white);font-size:13px;font-weight:700;white-space:nowrap}

/* hero */
.hero{position:absolute;left:0;top:73px;width:1200px;height:542px;background:var(--navy)}
.hero-photo{left:256px;top:-12px;width:944px;height:554px;background:linear-gradient(180deg,#cfdfe8 0%,#9fbfd2 30%,#4f7f8c 48%,#2b5a3a 62%,#1e3f22 85%,#16301c 100%)}
.hero-box{position:absolute;left:256px;top:143px;width:354px;height:200px;background:var(--navy)}
.hero-rule{position:absolute;left:59px;top:177px;width:2px;height:166px;background:var(--white)}
.hero-title{position:absolute;left:90px;top:168px;line-height:63px;font-size:48px;text-transform:uppercase}
.hero-title .thin{color:var(--green);font-weight:400;display:block}
.hero-title .bold{color:var(--white);font-weight:700;display:block;font-size:50px}
.btn{position:absolute;display:flex;height:44px;font-size:13.5px;font-weight:700}
.btn .label{display:flex;align-items:center;padding:0 24px;background:var(--btn);color:var(--white)}
.btn .arrow{width:40px;display:flex;align-items:center;justify-content:center;background:var(--green)}
.btn.light .label{background:var(--white);color:var(--btn)}

/* solutions */
.solutions{position:absolute;left:0;top:615px;width:1200px;height:514px;background:var(--light);overflow:hidden}
.section-title{position:absolute;left:0;width:1200px;text-align:center;font-size:30px;font-weight:700;color:var(--ink);text-transform:uppercase}
.about-title{position:absolute;left:56px;top:193px;font-size:20px;font-weight:700;color:var(--teal)}
.about-text{position:absolute;left:56px;top:232px;width:540px;font-size:12.8px;line-height:22.4px;color:var(--text)}
.teal-back{position:absolute;left:901px;top:296px;width:169px;height:127px;background:var(--teal-dark)}

/* features */
.feature{position:absolute;top:1164px;width:330px;text-align:center}
.feature-ring{position:relative;margin:0 auto;width:172px;height:172px;border-radius:50%;background:#eef1f0}
.feature-num{position:absolute;left:0;top:28px;width:172px;font-size:110px;font-weight:900;color:transparent;-webkit-text-stroke:2px #d8e9cc;line-height:110px;letter-spacing:-4px}
.feature-label{position:absolute;left:0;top:74px;width:172px;font-size:17px;font-weight:700;color:var(--teal)}
.feature p{margin-top:20px;font-size:12.8px;line-height:20px;color:var(--text)}
.feature .more{display:block;margin-top:12px;font-size:13px;font-weight:700;color:var(--teal)}

/* video */
.video{left:56px;top:1487px;width:1088px;height:313px;background:linear-gradient(135deg,#2a2a18 0%,#4a3412 35%,#6b4214 55%,#3a2c12 80%,#1f2212 100%)}
.video-label{position:absolute;left:56px;top:1598px;width:1088px;text-align:center;color:var(--white);font-size:19px}

/* best */
.best-kicker{position:absolute;left:216px;top:1868px;font-size:19px;color:var(--green)}
.best-title{position:absolute;left:216px;top:1902px;font-size:30px;font-weight:700;color:var(--ink)}
.best-rule{position:absolute;left:490px;top:1848px;width:1px;height:114px;background:#b9c7a6}
.perk{position:absolute;display:flex;align-items:center;gap:14px;font-size:13px;color:var(--text);white-space:nowrap}

/* testimonial */
.testimonial{position:absolute;left:0;top:2022px;width:1200px;height:354px;background:var(--light);overflow:hidden}
.quote-head{position:absolute;left:323px;top:42px;width:480px;font-size:20px;font-weight:700;line-height:28px;color:var(--ink)}
.quote-body{position:absolute;left:357px;top:128px;width:665px;font-size:12.8px;line-height:20px;color:var(--text)}
.quote-mark{font-size:22px;font-weight:700;color:var(--ink)}
.quote-name{position:absolute;left:357px;top:270px;font-size:16.5px;font-weight:700;color:var(--teal)}
.quote-role{position:absolute;left:357px;top:295px;font-size:15.5px;color:var(--text)}

/* clients */
.clients-row{position:absolute;left:0;top:2482px;width:1200px;height:60px}
.client{position:absolute;top:18px;width:130px;margin-left:-65px;font-size:15px;font-weight:700;color:var(--teal);display:flex;align-items:center;justify-content:center;gap:6px;white-space:nowrap}
.client .mark{width:14px;height:14px;border-radius:50%;background:var(--teal);flex:none}

/* contact */
.contact-title{position:absolute;left:57px;top:2588px;font-size:20px;font-weight:700;color:var(--teal)}
.contact-lead{position:absolute;left:57px;top:2636px;width:390px;font-size:15.5px;line-height:20px;color:var(--text)}
.field{position:absolute;border:1px solid var(--green);background:var(--white);font-size:13px;color:var(--text);padding:13px 9px}
.send{position:absolute;left:56px;top:2948px;width:86px;height:35px;background:var(--btn);color:var(--white);font-size:13.5px;font-weight:700;display:flex;align-items:center;justify-content:center}
.map{left:582px;top:2600px;width:618px;height:416px;background:linear-gradient(180deg,#eceeee,#e2e5e6)}
.contact-card{position:absolute;left:513px;top:2647px;width:303px;height:320px;background:var(--teal);border-radius:10px;color:var(--white);overflow:hidden}
.contact-card h3{position:absolute;left:29px;top:24px;font-size:20px;font-weight:700}
.card-row{position:absolute;left:29px;display:flex;gap:16px;font-size:15.5px;line-height:20px;width:265px}
.card-row svg{flex:none}
.card-dot{position:absolute;left:222px;top:250px;width:70px;height:70px;border-radius:50%;background:var(--green)}

.site-footer{position:absolute;left:0;top:3016px;width:1200px;height:30px;background:var(--navy);color:var(--white);font-size:12px;text-align:center;line-height:30px}
</style>
</head>
<body>

<header class="site-header">
  <div class="brand"><span class="brand-dot"></span>Velmora</div>
  <nav>
    <span class="nav-item active" style="left:274px">Odour Control Products</span>
    <span class="nav-item" style="left:446px">How Biofiltration Works</span>
    <span class="nav-item" style="left:603px">Odour Control by Industry</span>
    <span class="nav-item" style="left:771px">Past Projects</span>
    <span class="nav-item" style="left:867px">About Us</span>
    <span class="nav-item" style="left:941px">Contact</span>
  </nav>
  <div class="header-phone">
    <svg width="20" height="20" viewBox="0 0 24 24"><path fill="#7cb83a" d="M6.6 10.8a15 15 0 0 0 6.6 6.6l2.2-2.2c.3-.3.7-.4 1-.2 1.1.4 2.3.6 3.6.6.6 0 1 .4 1 1V20c0 .6-.4 1-1 1A17 17 0 0 1 3 4c0-.6.4-1 1-1h3.5c.6 0 1 .4 1 1 0 1.3.2 2.5.6 3.6.1.3 0 .7-.2 1z"/></svg>
    +61 (08) 5550 0142
  </div>
</header>

<section class="hero">
  <div class="img-fill hero-photo" role="img" aria-label="Forested valley under a cloudy sky"></div>
  <div class="hero-box"></div>
  <div class="hero-rule"></div>
  <h1 class="hero-title"><span class="thin">Odours</span><span class="bold">Controlled</span><span class="thin">Naturally</span></h1>
  <div class="btn light" style="left:422px;top:343px">
    <span class="label">Request a Quote</span>
    <span class="arrow"><svg width="22" height="16" viewBox="0 0 22 16"><path d="M1 8h19M13 1l7 7-7 7" stroke="#fff" stroke-width="2.2" fill="none"/></svg></span>
  </div>
</section>

<section class="solutions">
  <svg class="abs" style="left:0;top:0" width="1200" height="514">
    <polygon points="885,0 1200,0 1200,250" fill="#15607c"/>
    <polygon points="0,240 0,514 258,514" fill="#c7cdce"/>
  </svg>
  <h2 class="section-title" style="top:46px">Odour Control Solutions</h2>
  <h3 class="about-title">About Velmora</h3>
  <p class="about-text">Velmora uses sustainable biotechnology to resolve odour and corrosion problems in a highly efficient, environmentally friendly and cost-effective manner. Our products, the Velvent series of biofilters have been specifically engineered to overcome issues traditionally associated with biofiltration, such as bed compaction and uneven moisture levels, and our patented design achieves a removal rate of up to 99.9% per stage of treatment.</p>
  <div class="btn" style="left:56px;top:364px">
    <span class="label">Request A Quote</span>
    <span class="arrow"><svg width="22" height="16" viewBox="0 0 22 16"><path d="M1 8h19M13 1l7 7-7 7" stroke="#fff" stroke-width="2.2" fill="none"/></svg></span>
  </div>
  <div class="teal-back"></div>
  <div class="img-fill" style="left:754px;top:190px;width:149px;height:106px;background:linear-gradient(180deg,#3d6b3a,#5aa7b0)" role="img" aria-label="Waterfall in a rainforest"></div>
  <div class="img-fill" style="left:910px;top:129px;width:234px;height:167px;background:linear-gradient(180deg,#c9d4c2,#8a9a78)" role="img" aria-label="Two people walking on a garden path"></div>
  <div class="img-fill" style="left:667px;top:306px;width:234px;height:168px;background:linear-gradient(180deg,#a9c3dc,#4f7fa4 55%,#5f8a3e)" role="img" aria-label="Person on a bench facing white sea cliffs"></div>
  <div class="img-fill" style="left:910px;top:306px;width:150px;height:107px;background:linear-gradient(180deg,#c7557f,#8c3f5c 60%,#4a7a2e)" role="img" aria-label="Avenue of blossoming trees"></div>
</section>

<div class="feature" style="left:56px">
  <div class="feature-ring"><div class="feature-num">01</div><div class="feature-label">PRODUCTS</div></div>
  <p>Utilising the same sustainable technology and patented design as the Velvent® VHM, the VPX module is Velmora’s above-ground solution, specifically designed to treat and control odours at higher flow rates.</p>
  <span class="more">Read More</span>
</div>
<div class="feature" style="left:434px">
  <div class="feature-ring"><div class="feature-num">02</div><div class="feature-label">FEATURES</div></div>
  <p>Velmora® products fully comply with WSA 121-2004 Industry Standard for Biofilters for Odour Control. The enclosed design allows for treatment conditions to be tightly controlled</p>
  <span class="more">Read More</span>
</div>
<div class="feature" style="left:816px">
  <div class="feature-ring"><div class="feature-num">03</div><div class="feature-label">PAST PROJECTS</div></div>
  <p>The Harlow Street Wastewater Pump Station had been causing odour issues for the Coastal Water Authority for many years. Despite large land buffers around the pump</p>
  <span class="more">Read More</span>
</div>

<div class="img-fill video" role="img" aria-label="Aerial view of rolling farmland at dusk"></div>
<div class="video-label">WATCH OUR VIDEO</div>
<svg class="abs" style="left:574px;top:1638px" width="50" height="50" viewBox="0 0 50 50"><circle cx="25" cy="25" r="23" stroke="#fff" stroke-width="2" fill="none"/><path d="M20 15l14 10-14 10z" fill="#fff"/></svg>

<div class="best-kicker">What makes</div>
<div class="best-title">US THE BEST?</div>
<div class="best-rule"></div>
<div class="perk" style="left:553px;top:1848px"><svg width="12" height="12" viewBox="0 0 12 12"><path d="M1 6l3.5 3.5L11 2" stroke="#7cb83a" stroke-width="2" fill="none"/></svg>Biological &amp; Sustainable technology</div>
<div class="perk" style="left:823px;top:1849px"><svg width="12" height="12" viewBox="0 0 12 12"><path d="M1 6l3.5 3.5L11 2" stroke="#7cb83a" stroke-width="2" fill="none"/></svg>100% Australian Owned</div>
<div class="perk" style="left:553px;top:1888px"><svg width="12" height="12" viewBox="0 0 12 12"><path d="M1 6l3.5 3.5L11 2" stroke="#7cb83a" stroke-width="2" fill="none"/></svg>Efficient maintenance cost</div>
<div class="perk" style="left:823px;top:1889px"><svg width="12" height="12" viewBox="0 0 12 12"><path d="M1 6l3.5 3.5L11 2" stroke="#7cb83a" stroke-width="2" fill="none"/></svg>Eco Friendly</div>
<div class="btn" style="left:553px;top:1929px">
  <span class="label">Request A Quote</span>
  <span class="arrow"><svg width="22" height="16" viewBox="0 0 22 16"><path d="M1 8h19M13 1l7 7-7 7" stroke="#fff" stroke-width="2.2" fill="none"/></svg></span>
</div>

<section class="testimonial">
  <svg class="abs" style="left:0;top:0" width="1200" height="354">
    <polygon points="885,0 1200,0 1200,260" fill="#c7cdce"/>
    <polygon points="0,90 0,354 250,354" fill="#7cb83a"/>
  </svg>
  <div class="img-fill" style="left:146px;top:74px;width:170px;height:170px;border-radius:50%;background:linear-gradient(180deg,#d9a25c,#c9743a 55%,#e9e3dc)" role="img" aria-label="Portrait of a satisfied local resident"></div>
  <h3 class="quote-head">AS SOON AS THE SYSTEM WAS STARTED, THE SMELL DISAPPEARED!</h3>
  <p class="quote-body"><span class="quote-mark">“</span> Marcus and the Velmora team promised to stop the odour from our smelly neighbor and they delivered- in spades! As soon as the system was started, the smell disappeared. The system is well designed, very professionally installed and the beauty of it is, apart from a constantly running fan, it is bacteria doing the heavy lifting, so it is very environmentally friendly. We lived with the smell for 3 three years which could be extremely frustrating and unpleasant. Now, the problem is solved and we can have BBQs again. We are happy and our neighbours have noticed the odour is gone. Thank you! <span class="quote-mark">”</span></p>
  <div class="quote-name">Sam Ellery</div>
  <div class="quote-role">Nearby resident to Harlow Street Wastewater Pump Station</div>
</section>

<h2 class="section-title" style="top:2410px">Our Happy Clients</h2>
<div class="clients-row">
  <svg class="abs" style="left:185px;top:15px" width="32" height="32"><circle cx="16" cy="16" r="14" stroke="#7cb83a" stroke-width="2" fill="none"/><path d="M18 10l-6 6 6 6" stroke="#7cb83a" stroke-width="2" fill="none"/></svg>
  <div class="client" style="left:335px"><span class="mark"></span>Clearwater</div>
  <div class="client" style="left:482px">Redgum Territory</div>
  <div class="client" style="left:615px">Riverton City</div>
  <div class="client" style="left:746px">Sandbay City</div>
  <div class="client" style="left:881px"><span class="mark"></span>Ridgeline Water</div>
  <svg class="abs" style="left:983px;top:15px" width="32" height="32"><circle cx="16" cy="16" r="14" stroke="#7cb83a" stroke-width="2" fill="none"/><path d="M14 10l6 6-6 6" stroke="#7cb83a" stroke-width="2" fill="none"/></svg>
</div>

<h2 class="contact-title">GET IN CONTACT</h2>
<p class="contact-lead">If you have any queries regarding out products, please do not hesitate to contact us</p>
<div class="field" style="left:56px;top:2693px;width:204px;height:44px">First Name</div>
<div class="field" style="left:266px;top:2693px;width:203px;height:44px">Surname</div>
<div class="field" style="left:58px;top:2745px;width:411px;height:44px">Email</div>
<div class="field" style="left:56px;top:2796px;width:411px;height:44px">Phone</div>
<div class="field" style="left:56px;top:2849px;width:411px;height:86px">Message</div>
<div class="send">SEND</div>

<div class="img-fill map" role="img" aria-label="Street map showing the office location"></div>
<div class="contact-card">
  <h3>CONTACT US</h3>
  <div class="card-row" style="top:76px"><svg width="24" height="22" viewBox="0 0 24 24"><path fill="none" stroke="#7cb83a" stroke-width="1.6" d="M6.6 10.8a15 15 0 0 0 6.6 6.6l2.2-2.2c.3-.3.7-.4 1-.2 1.1.4 2.3.6 3.6.6.6 0 1 .4 1 1V20c0 .6-.4 1-1 1A17 17 0 0 1 3 4c0-.6.4-1 1-1h3.5c.6 0 1 .4 1 1 0 1.3.2 2.5.6 3.6.1.3 0 .7-.2 1z"/></svg>+61 (08) 5550 0142</div>
  <div class="card-row" style="top:121px"><svg width="24" height="20" viewBox="0 0 24 20"><rect x="1" y="3" width="22" height="14" fill="none" stroke="#7cb83a" stroke-width="1.6"/><path d="M1 3l11 8 11-8" fill="none" stroke="#7cb83a" stroke-width="1.6"/></svg>info@velmora-sample.com.au</div>
  <div class="card-row" style="top:156px"><svg width="24" height="24" viewBox="0 0 24 24"><circle cx="12" cy="12" r="11" fill="none" stroke="#7cb83a" stroke-width="1.6"/></svg>www.socialnet.example/<br>company/velmora/</div>
  <div class="card-row" style="top:212px"><svg width="24" height="26" viewBox="0 0 24 26"><path d="M12 25s8-9 8-15a8 8 0 0 0-16 0c0 6 8 15 8 15z" fill="none" stroke="#7cb83a" stroke-width="1.6"/><circle cx="12" cy="10" r="3" fill="none" stroke="#7cb83a" stroke-width="1.6"/></svg>12 Banksia Court,<br>Greenvale WA 6000,<br>Australia</div>
  <div class="card-dot"></div>
</div>

<footer class="site-footer">Privacy Policy &nbsp;| Sitemap &nbsp;| ABN: 12 345 678 901</footer>

</body>
</html>
```